Brivet Networks, Inc. Website redesign

Revamp the website, it is old and outdated. www.brivetnetworksinc.com

Target Market(s)

Information Technology Consulting and Staffing

Coding

Coded - Design and coding required

Number of Pages Required

5+ page

Colors

Designer to choose colors to be used in the design.

Requirements
Must have
• Outlined text boxes just like from the Hollis.us site. A clean look

```html
<!DOCTYPE html>
<html lang="en">
<head>
<meta charset="utf-8">
<title>Brivet Networks, Inc. — IT Consulting</title>
<link href="https://fonts.googleapis.com/css2?family=Roboto:wght@300;400;500;700&family=Oswald:wght@700&family=Roboto+Condensed:wght@700&display=swap" rel="stylesheet">
<style>
:root{
  --red:#a01b31;
  --red-btn:#c2132f;
  --ink:#1c1c1c;
  --muted:#6d6d6d;
  --gray-bg:#e8e8e8;
  --light-bg:#f7f7f7;
  --footer:#161616;
  --white:#fff;
}
*{margin:0;padding:0;box-sizing:border-box}
html,body{width:1200px;height:3523px;overflow:hidden}
body{position:relative;font-family:"Roboto",sans-serif;color:var(--ink);background:var(--white)}
.abs{position:absolute}
.btn{position:absolute;background:var(--red-btn);color:#fff;font-weight:700;text-transform:uppercase;display:flex;align-items:center;justify-content:center}
.btn-sm{height:25px;font-size:11px;padding:0 10px}
.section-title{position:absolute;left:0;width:1200px;text-align:center;font-family:"Roboto Condensed",sans-serif;font-weight:700;font-size:37px;color:var(--ink)}

/* top bar */
.topbar{left:0;top:0;width:1200px;height:31px;border-bottom:1px solid #ddd;font-size:11px;color:#333}
.topbar .contact{position:absolute;left:94px;top:8px;display:flex;gap:14px;align-items:center}
.topbar .follow{position:absolute;right:94px;top:7px;display:flex;gap:6px;align-items:center}
.dot{width:16px;height:16px;border-radius:50%;background:#3a5a98;display:inline-block}
.dot.li{background:#1b76b3}

/* nav */
.nav{left:0;top:31px;width:1200px;height:66px}
.brand{position:absolute;left:94px;top:20px}
.brand .name{font-weight:700;font-size:22px;color:var(--ink);letter-spacing:.5px}
.menu{position:absolute;right:94px;top:26px;display:flex;gap:33px;font-size:11px}
.menu .active{color:var(--red-btn);border-bottom:1px solid var(--red-btn);padding-bottom:5px}

/* hero */
.hero{left:0;top:97px;width:1200px;height:502px;background:linear-gradient(100deg,#6f757c 0%,#3c4148 35%,#20252b 60%,#15181c 100%)}
.hero .l1{left:685px;top:133px;color:#fff;font-family:"Roboto Condensed",sans-serif;font-size:31px;font-weight:700}
.hero .l2{left:683px;top:165px;color:#d8142f;font-family:"Oswald",sans-serif;font-size:82px;font-weight:700;line-height:1;letter-spacing:-1px}
.hero .l3{left:687px;top:268px;color:#fff;font-size:20px;font-weight:700;letter-spacing:6px}
.hero .btn{left:697px;top:312px;width:153px;height:52px;font-size:18px}
.hero .pager{left:1005px;top:443px;color:#fff;font-size:28px;display:flex;align-items:baseline;gap:6px}
.hero .pager small{font-size:18px}
.hero .pager i{display:inline-block;width:36px;height:1px;background:#fff;vertical-align:middle}

/* services */
.svc{position:absolute;top:728px;width:237px;height:264px;text-align:center}
.svc.active{background:var(--red)}
.svc .icon{width:96px;height:96px;margin:34px auto 0;border-radius:50%;border:4px solid var(--red);background:#fff;display:flex;align-items:center;justify-content:center}
.svc.active .icon{border-color:#111}
.svc p{font-size:11px;line-height:18px;color:#777;margin:14px 22px 0}
.svc.active p{color:#f4d6db}
.svc .btn{left:50%;transform:translateX(-50%);top:205px}
.svc.active .btn{background:#111}

/* about */
.about{left:0;top:1057px;width:1200px;height:503px;background:var(--gray-bg)}
.about .frame{left:94px;top:37px;width:160px;height:429px;background:var(--red)}
.about .photo{left:126px;top:62px;width:509px;height:379px;background:linear-gradient(90deg,#4d5563,#b9c2cf 45%,#d8dde4 55%,#465060)}
.about .kicker{left:668px;top:88px;font-size:23px;color:var(--red)}
.about h2{position:absolute;left:666px;top:118px;font-family:"Roboto Condensed",sans-serif;font-size:36px;font-weight:700}
.about .copy{left:668px;top:170px;width:440px;font-size:11px;line-height:18px;color:#666}
.about .copy p{margin-bottom:8px}
.about .btn{left:668px;top:379px;width:112px;height:32px;font-size:13px}

/* leaders */
.arrow{position:absolute;top:1760px;width:32px;height:32px;border:1px solid #999;background:#fff;display:flex;align-items:center;justify-content:center}
.arrow.next{border-color:var(--red)}
.leader-photo{left:521px;top:1683px;width:157px;height:157px;border-radius:50%;border:6px solid var(--red);background:radial-gradient(circle,#8a8a8a,#2a2a2a)}
.leader-name{left:0;top:1860px;width:1200px;text-align:center;font-size:18px}
.leader-bio{left:130px;top:1894px;width:940px;text-align:center;font-size:11px;line-height:18px;color:#777}

/* strategy */
.strategy-bg{left:0;top:2196px;width:1200px;height:362px;background:var(--light-bg)}
.strategy-img{left:565px;top:2052px;width:635px;height:475px;background:linear-gradient(120deg,#0b1f3e,#1b5c9a 40%,#3fa4da 60%,#0c2a52)}
.strategy .kicker{left:94px;top:2147px;font-size:23px;color:var(--red)}
.strategy h2{position:absolute;left:94px;top:2177px;font-family:"Roboto Condensed",sans-serif;font-size:36px;font-weight:700}
.strategy-box{left:94px;top:2233px;width:560px;height:325px;background:var(--red)}
.strategy-box p{position:absolute;left:41px;top:53px;width:482px;font-size:11px;line-height:18px;color:#f2dfe2}
.strategy-box .btn{left:42px;top:250px;width:112px;height:33px;font-size:13px;border-left:4px solid #7d0f1f}

/* news */
.news{position:absolute;top:2692px;width:323px}
.news .img{height:247px}
.news .date{margin-top:16px;font-size:11px;color:var(--red-btn)}
.news h3{font-size:18px;font-weight:500;line-height:24px;margin-top:4px}
.news p{font-size:11px;line-height:18px;color:#777;margin-top:8px}
.news .btn{position:relative;display:inline-flex;margin-top:12px}

/* footer */
.footer{left:0;top:3181px;width:1200px;height:301px;background:var(--footer);color:#ddd}
.footer .panel{left:94px;top:0;width:337px;height:301px;background:var(--red);color:#fff}
.footer .panel .name{position:absolute;left:28px;top:56px;font-size:26px;font-weight:700}
.footer .panel p{position:absolute;left:28px;top:146px;width:280px;font-size:11px;line-height:18px}
.footer .panel .follow{position:absolute;left:28px;top:230px;font-size:17px;display:flex;align-items:center;gap:8px}
.footer .panel .follow .dot{width:24px;height:24px;background:#fff}
.fcol{position:absolute;top:80px;font-size:11px}
.fcol h4{font-size:14px;font-weight:500;color:#fff;padding-bottom:4px;border-bottom:2px solid #fff;display:inline-block;margin-bottom:8px}
.fcol li{list-style:none;line-height:25px}
.fcol li::before{content:"▸ ";font-size:8px}
.fcol .row{display:flex;gap:8px;line-height:17px;margin-bottom:10px}
.bottom{left:0;top:3482px;width:1200px;height:41px;background:var(--red);color:#f0cfd4;font-size:11px}
.bottom span{position:absolute;top:14px}
</style>
</head>
<body>

<header class="abs topbar">
  <div class="contact">
    <span><svg width="11" height="11" viewBox="0 0 24 24"><path fill="#c2132f" d="M6.6 10.8a15 15 0 006.6 6.6l2.2-2.2c.3-.3.7-.4 1-.2 1.1.4 2.3.6 3.6.6.6 0 1 .4 1 1V20c0 .6-.4 1-1 1A17 17 0 013 4c0-.6.4-1 1-1h3.5c.6 0 1 .4 1 1 0 1.3.2 2.5.6 3.6.1.3 0 .7-.2 1z"/></svg> 301-555-0172</span>
    <span><svg width="12" height="9" viewBox="0 0 24 18"><rect width="24" height="18" fill="#c2132f"/><path d="M0 0l12 10L24 0" stroke="#fff" fill="none" stroke-width="2"/></svg> info@brivetnetworks.com</span>
  </div>
  <div class="follow">Follow Us: <i class="dot"></i><i class="dot li"></i></div>
</header>

<nav class="abs nav">
  <div class="brand"><span class="name">BRIVET NETWORKS</span></div>
  <div class="menu"><span class="active">Home</span><span>About us</span><span>Services</span><span>Strategy</span><span>IT News</span><span>Contact us</span></div>
</nav>

<section class="abs hero" role="img" aria-label="Photo of network switches and patch cables in a server rack">
  <div class="abs l1">BRINGING THOUGHT</div>
  <div class="abs l2">LEADERSHIP</div>
  <div class="abs l3">&amp; QUALITY TO EVERY PROJECT</div>
  <div class="btn">CONTACT US</div>
  <div class="abs pager">01 <small>02</small> <i></i></div>
</section>

<h2 class="section-title" style="top:658px">SERVICES</h2>

<div class="svc" style="left:94px">
  <div class="icon"><svg width="44" height="44" viewBox="0 0 44 44"><rect x="6" y="8" width="18" height="28" fill="#111"/><circle cx="30" cy="24" r="10" fill="#111"/><circle cx="30" cy="24" r="3" fill="#fff"/></svg></div>
  <p>We have access to multiple distributor partners throughout North America, as well as Elite Partner Status with</p>
  <div class="btn btn-sm">Read More</div>
</div>
<div class="svc active" style="left:353px">
  <div class="icon"><svg width="46" height="44" viewBox="0 0 46 44"><circle cx="16" cy="13" r="7" fill="#111"/><circle cx="30" cy="15" r="7" fill="#111"/><path d="M3 38c0-9 6-14 13-14s13 5 13 14zM20 38c1-8 5-12 10-12 7 0 12 5 12 12z" fill="#111"/></svg></div>
  <p>We have access to multiple distributor partners throughout North America, as well as Elite Partner Status with</p>
  <div class="btn btn-sm">Read More</div>
</div>
<div class="svc" style="left:611px">
  <div class="icon"><svg width="44" height="44" viewBox="0 0 44 44"><circle cx="18" cy="20" r="10" fill="#111"/><rect x="14" y="30" width="8" height="8" fill="#111"/><circle cx="32" cy="10" r="5" fill="none" stroke="#111" stroke-width="3"/></svg></div>
  <p>We have access to multiple distributor partners throughout North America, as well as Elite Partner Status with</p>
  <div class="btn btn-sm">Read More</div>
</div>
<div class="svc" style="left:870px">
  <div class="icon"><svg width="46" height="46" viewBox="0 0 46 46"><circle cx="23" cy="23" r="12" fill="none" stroke="#111" stroke-width="5" stroke-dasharray="5 3"/><circle cx="23" cy="23" r="5" fill="#111"/><path d="M23 2v6M23 38v6M2 23h6M38 23h6" stroke="#111" stroke-width="3"/></svg></div>
  <p>We have access to multiple distributor partners throughout North America, as well as Elite Partner Status with</p>
  <div class="btn btn-sm">Read More</div>
</div>

<section class="abs about">
  <div class="abs frame"></div>
  <div class="abs photo" role="img" aria-label="Photo of a smiling consultant holding a tablet in a data center aisle"></div>
  <div class="abs kicker">ABOUT US</div>
  <h2>BRIVET NETWORKS</h2>
  <div class="abs copy">
    <p>Brivet Networks, Inc. is an 8(a) innovative and rapidly growing full-service IT consulting firm. We provide our clients with cutting-edge technologies and the know-how to apply them to their individual business models.</p>
    <p>For over 20 + years, we have been providing reliable IT solutions to businesses in the Washington, DC Metro area and beyond. Our comprehensive services provide clients with unique technology solutions that are customized to meet the specific demands of their business.</p>
    <p>Look to our experts for strategic IT guidance, management and services that allows you to take your mind off technology and concentrate on your core area of business. Brivet Networks, Inc. provides cost-efficient solutions that simply make good sense.</p>
  </div>
  <div class="btn">READ MORE</div>
</section>

<h2 class="section-title" style="top:1616px">OUR LEADERS</h2>
<div class="arrow" style="left:124px"><svg width="10" height="14"><path d="M8 1L2 7l6 6" stroke="#555" stroke-width="2" fill="none"/></svg></div>
<div class="arrow next" style="left:1040px"><svg width="10" height="14"><path d="M2 1l6 6-6 6" stroke="#a01b31" stroke-width="2" fill="none"/></svg></div>
<div class="abs leader-photo" role="img" aria-label="Portrait photo of the chief technology officer"></div>
<div class="abs leader-name"><b>Darren Whitfield</b> - Chief Technology Officer</div>
<div class="abs leader-bio">Darren has played a leading role in the global information technology industry for more than 20 years, managing divisions and business the United States. Since founding Brivet Networks, Inc. (BNI) in 2008, he has been instrumental in formulating the company's strategy and building and managing the organization's core competencies. A member of BNI's Board of Directors, Darren now spends even more time traveling extensively to meet clients.</div>
<div class="btn btn-sm" style="left:559px;top:1960px">Read More</div>

<div class="abs strategy-bg"></div>
<div class="abs strategy-img" role="img" aria-label="Illustration of glowing blue network nodes and data blocks"></div>
<div class="strategy">
  <div class="abs kicker">OUR STRATEGY</div>
  <h2>YOUR PATH TO SUCCESS</h2>
</div>
<div class="abs strategy-box">
  <p>Civilian and Federal agencies are facing increased demands driven by the changing economic environment and shifts in the way products and services are sold and delivered. These factors have created an imperative to leverage new and innovative technology solution architectures like cloud computing to help reduce cost and deliver profit-driving IT capabilities faster than ever before. Savvy businesses understand that technology investments cannot be made solely to enable internal and external operations, technology is now, more than ever, a critical component to retaining and winning customers as well as staying ahead of the competition. Leadership have the opportunity to introduce application, process and technology changes that improve business efficiency and effectiveness, ultimately elevating the status of IT within the enterprise.</p>
  <div class="btn">READ MORE</div>
</div>

<h2 class="section-title" style="top:2617px">LATEST IT NEWS</h2>
<article class="news" style="left:94px">
  <div class="img" role="img" aria-label="Photo of a hand touching glowing cloud interface icons" style="background:linear-gradient(135deg,#0a3a8a,#2d82d8 50%,#0b2f6e)"></div>
  <div class="date">05 AUGUST, 2019</div>
  <h3>There are many variations of passages of Lorem Ipsum</h3>
  <p>It is a long established fact that a reader will be distracted by the readable content of a page when looking at its layout. The point of using Lorem Ipsum</p>
  <div class="btn btn-sm">Read More</div>
</article>
<article class="news" style="left:439px">
  <div class="img" role="img" aria-label="Photo of a network switch with many patch cables" style="background:linear-gradient(180deg,#dfe3ea,#7f8aa3 45%,#8d96b8)"></div>
  <div class="date">08 AUGUST, 2019</div>
  <h3>There are many variations of passages of Lorem Ipsum</h3>
  <p>It is a long established fact that a reader will be distracted by the readable content of a page when looking at its layout. The point of using Lorem Ipsum</p>
  <div class="btn btn-sm">Read More</div>
</article>
<article class="news" style="left:784px">
  <div class="img" role="img" aria-label="Photo of a hand holding a smartphone with floating app icons" style="background:linear-gradient(135deg,#cfd6de,#eef0f2 50%,#b9a79a)"></div>
  <div class="date">04 AUGUST, 2019</div>
  <h3>There are many variations of passages of Lorem Ipsum</h3>
  <p>It is a long established fact that a reader will be distracted by the readable content of a page when looking at its layout. The point of using Lorem Ipsum</p>
  <div class="btn btn-sm">Read More</div>
</article>

<footer class="abs footer">
  <div class="abs panel">
    <div class="name">BRIVET NETWORKS</div>
    <p>Brivet Networks, Inc. is an 8(a) innovative and rapidly growing full-service IT consulting firm. We provide our clients with cutting-edge technologies and the know-how to apply them to their individual business</p>
    <div class="follow">Follow Us: <i class="dot"></i><i class="dot"></i></div>
  </div>
  <div class="fcol" style="left:511px"><h4>QUICK LINK</h4><ul><li>Home</li><li>About us</li><li>Services</li><li>Strategy</li><li>IT News</li><li>Contact us</li></ul></div>
  <div class="fcol" style="left:716px"><h4>SERVICES</h4><ul><li>Hardware / Software Sales</li><li>Professional Services</li><li>Technology Assessment</li><li>Technology Consulting</li></ul></div>
  <div class="fcol" style="left:970px"><h4>CONTACT US</h4>
    <div class="row"><svg width="11" height="11" viewBox="0 0 24 24"><path fill="#fff" d="M6.6 10.8a15 15 0 006.6 6.6l2.2-2.2c.3-.3.7-.4 1-.2 1.1.4 2.3.6 3.6.6.6 0 1 .4 1 1V20c0 .6-.4 1-1 1A17 17 0 013 4c0-.6.4-1 1-1h3.5c.6 0 1 .4 1 1 0 1.3.2 2.5.6 3.6.1.3 0 .7-.2 1z"/></svg>301-555-0172</div>
    <div class="row"><svg width="12" height="9" viewBox="0 0 24 18"><rect width="24" height="18" fill="#fff"/><path d="M0 0l12 10L24 0" stroke="#161616" fill="none" stroke-width="2"/></svg>info@brivetnetworks.com</div>
    <div class="row"><svg width="11" height="14" viewBox="0 0 12 16"><path fill="#fff" d="M6 0a6 6 0 00-6 6c0 4.5 6 10 6 10s6-5.5 6-10a6 6 0 00-6-6zm0 8.5A2.5 2.5 0 116 3.5a2.5 2.5 0 010 5z"/></svg><span>Brivet Networks, Inc.<br>2280 Oakridge Ln<br>Fairmont, MD 20910</span></div>
  </div>
</footer>
<div class="abs bottom"><span style="left:96px">© 2019 brivetnetworks. All Right Reserved.</span><span style="right:94px">Policy &nbsp;|&nbsp; Contact Us</span></div>

</body>
</html>
```